New Business Card Design Project

Easy part first... I want the backside to be simple... jet black background with our logo in jet black/white/color. Feel free to play with tagline ideas under the logo if you want, I'm still toying around with it myself.

The front side... I need the logo on it, my photo headshot, and the following information:

Ray T. Calloway
Top Producer
555-201-4837
calloway.ray.t@fernmail.example
www.listnorthernnests.example
www.getnorthernnests.example

I'm looking for creativity with font, simple, but elegant, pairs well with the logo, good visibility of my photo, black background on the front as well, clearly see and identify information.
Updates

I would like the websites to have capitalization on the first letter of each word - www.ListNorthernNests.example and www.GetNorthernNests.example Also, I would like each of the capital letters to be slightly larger than the other font

Target Market(s)

We help people buy and sell homes from $50,000 to over a $1million.

Industry/Entity Type

Business

Requirements
Must have
• Must have information from above.
Nice to have
• Introducing a new color to be sharp against the black- possibly in the silver/nickel/platinum metallics? Feel free to crop the headshot down some if needed.
Should not have
• NO CHEESY GRAPHICS

```html
<!DOCTYPE html>
<html lang="en">
<head>
<meta charset="utf-8">
<title>Northern Nest Realty — Business Card</title>
<link rel="stylesheet" href="https://fonts.googleapis.com/css2?family=Cormorant+Garamond:ital,wght@0,500;0,600;1,500&display=swap">
<style>
  :root {
    --canvas: #ffffff;
    --card-black: #050505;
    --logo-black: #000000;
    --ink-white: #f4f4f2;
    --gold: #b5a47a;
    --photo-dark: #3a2c22;
    --photo-mid: #5b4636;
  }
  * { margin: 0; padding: 0; box-sizing: border-box; }
  html, body {
    width: 1200px; height: 900px; overflow: hidden;
    background: var(--canvas);
    font-family: "Cormorant Garamond", Georgia, serif;
    font-variant-numeric: lining-nums;
  }
  .canvas { position: relative; width: 1200px; height: 900px; }

  .card { position: absolute; background: var(--card-black); }
  .card--front { left: 273px; top: 33px; width: 659px; height: 402px; }
  .card--back  { left: 272px; top: 465px; width: 658px; height: 401px; }

  .brand-block {
    position: absolute; background: var(--logo-black);
    display: flex; align-items: center; justify-content: center;
    color: var(--ink-white); font-weight: 600; text-align: center;
    letter-spacing: 0.04em;
  }
  .card--front .brand-block {
    left: 38px; top: 25px; width: 167px; height: 104px;
    font-size: 21px; line-height: 1.1;
  }
  .card--back .brand-block {
    left: 119px; top: 50px; width: 438px; height: 273px;
    font-size: 46px; line-height: 1.1;
  }

  .agent { position: absolute; left: 32px; top: 151px; color: var(--ink-white); }
  .agent__name { font-size: 25px; font-weight: 500; line-height: 34px; }
  .agent__title { font-size: 22px; font-style: italic; font-weight: 500; color: var(--gold); line-height: 34px; }
  .agent__contact { margin-top: 30px; list-style: none; font-size: 20.5px; font-weight: 500; line-height: 31.3px; white-space: nowrap; }
  .cap { font-size: 1.14em; line-height: 1; }

  .headshot {
    position: absolute; left: 377px; top: 75px; width: 257px; height: 294px;
    background: radial-gradient(ellipse at 60% 40%, var(--photo-mid), var(--photo-dark) 75%);
  }
</style>
</head>
<body>
<div class="canvas">
  <section class="card card--front">
    <div class="brand-block">Northern Nest<br>Realty</div>
    <div class="agent">
      <p class="agent__name">Ray T. Calloway</p>
      <p class="agent__title">Top Producer</p>
      <ul class="agent__contact">
        <li>555-201-4837</li>
        <li>calloway.ray.t@fernmail.example</li>
        <li>www.<span class="cap">L</span>ist<span class="cap">N</span>orthern<span class="cap">N</span>ests.example</li>
        <li>www.<span class="cap">G</span>et<span class="cap">N</span>orthern<span class="cap">N</span>ests.example</li>
      </ul>
    </div>
    <div class="headshot" role="img" aria-label="Headshot of the agent in a dark suit and blue tie against a brown studio backdrop"></div>
  </section>

  <section class="card card--back">
    <div class="brand-block">Northern Nest<br>Realty</div>
  </section>
</div>
</body>
</html>
```